Vondrake - Waste to Fuel Power Needs A Website

Make website explaining the concept and the team behind the company
Updates

I will be providing A logo and Information about the company upon signed NDA.

Coding

Coded - Design and coding required

Number of Pages Required

5+ page

```html
<!DOCTYPE html>
<html lang="en">
<head>
<meta charset="utf-8">
<title>Vondrake - Waste to Fuel Power</title>
<link rel="stylesheet" href="https://fonts.googleapis.com/css2?family=Montserrat:wght@400;500;600;700;800;900&display=swap">
<style>
:root{
  --blue:#1e90d8;
  --blue-dark:#0d5f9c;
  --green:#8cc63f;
  --navy:#1b2735;
  --navy-2:#222f3e;
  --teal:#1b7f9e;
  --ink:#1a1a1a;
  --muted:#6b7480;
  --light:#f3f6f9;
  --white:#ffffff;
}
*{box-sizing:border-box;margin:0;padding:0}
html,body{width:1200px;height:5352px;overflow:hidden}
body{font-family:"Montserrat",Arial,sans-serif;color:var(--ink);background:var(--white);position:relative}
.ph{position:absolute}
.eyebrow{font-size:11px;font-weight:600;color:var(--green);letter-spacing:1px;text-transform:uppercase}
.h2{font-weight:900;text-transform:uppercase;line-height:1.05;color:var(--ink)}
.body{font-size:13px;line-height:1.7;color:var(--muted)}
.btn{display:inline-flex;align-items:center;gap:10px;background:var(--green);color:var(--white);font-size:12px;font-weight:700;text-transform:uppercase;padding:14px 26px;border-radius:4px}
.btn .dot{width:18px;height:18px;border-radius:50%;background:var(--white);display:inline-block}

/* Hero */
.hero{position:absolute;left:0;top:0;width:1200px;height:760px;background:linear-gradient(180deg,#0e3f7a 0%,#1d5fa3 40%,#3d7ab8 62%,#e79a4a 80%,#2b3d55 100%)}
.hero-shade{position:absolute;inset:0;background:linear-gradient(180deg,rgba(10,40,90,.55),rgba(10,40,90,.1) 60%,rgba(10,20,40,.5))}
.nav{position:absolute;left:60px;top:18px;width:1080px;height:60px;display:flex;align-items:center;justify-content:space-between}
.logo{display:flex;align-items:center;gap:10px;font-size:22px;font-weight:800;color:var(--white)}
.logo .mark{width:18px;height:18px;border-radius:50%;background:var(--green)}
.menu{display:flex;gap:34px;align-items:center;font-size:11px;font-weight:600;color:var(--white);text-transform:uppercase}
.menu .btn{padding:10px 18px;font-size:11px}
.hero-text{position:absolute;left:0;top:150px;width:1200px;text-align:center;color:var(--white)}
.hero-text h1{font-size:48px;font-weight:900;line-height:1.1;margin-top:10px;text-transform:uppercase}
.hero-text p{font-size:13px;line-height:1.6;width:560px;margin:14px auto 22px;opacity:.9}

/* Who */
.who-img1{left:160px;top:820px;width:110px;height:300px;background:linear-gradient(180deg,#e9eef2,#c5d3de)}
.who-img2{left:300px;top:815px;width:220px;height:400px;border-radius:0 60px 0 0;background:linear-gradient(160deg,#5cb6ef,#1e6fb8)}
.who-text{left:600px;top:860px;width:440px}
.who-text .h2{font-size:44px;margin:8px 0 16px}
.who-text p{margin-bottom:14px}

/* Process */
.process{left:0;top:1305px;width:1200px;height:380px;background:linear-gradient(180deg,#1d8bb0,#176f8f)}
.process-head{position:absolute;top:60px;width:1200px;text-align:center;color:var(--white)}
.process-head .h2{color:var(--white);font-size:34px;margin-top:6px}
.steps{position:absolute;left:170px;top:150px;width:860px;display:flex;gap:30px}
.step{flex:1;color:var(--white)}
.step .num{font-size:11px;font-weight:700;color:var(--green)}
.step h3{font-size:15px;font-weight:800;text-transform:uppercase;line-height:1.15;margin:4px 0 8px}
.step p{font-size:10px;line-height:1.6;opacity:.85}

/* Quality */
.quality-text{left:180px;top:1810px;width:420px}
.quality-text .h2{font-size:34px;margin:8px 0 14px}
.quality-text p{font-size:12px;margin-bottom:10px}
.quality-img{left:630px;top:1810px;width:370px;height:400px;border-radius:14px;background:linear-gradient(180deg,#7fb2d8,#a9b8c2 55%,#6f7f6a)}
.quality-frame{left:660px;top:1840px;width:370px;height:400px;border-radius:14px;border:10px solid var(--green);z-index:-1}
.badge{left:880px;top:2080px;width:140px;height:100px;background:var(--green);border-radius:10px;color:var(--white);text-align:center;padding-top:20px}
.badge b{font-size:36px;font-weight:800;display:block}
.badge span{font-size:10px;font-weight:600}

/* Impact */
.impact-head{left:0;top:2295px;width:1200px;text-align:center}
.impact-head .h2{font-size:34px;margin-top:6px}
.impact-head .body{width:760px;margin:10px auto 0;font-size:12px;line-height:1.6}
.cards{left:140px;top:2460px;width:920px;display:flex;gap:20px}
.card{flex:1;height:290px;background:var(--white);border-radius:6px;box-shadow:0 6px 24px rgba(0,0,0,.08);padding:26px 20px}
.card .ic{width:44px;height:44px;border-radius:50%;background:var(--light);margin-bottom:16px;display:flex;align-items:center;justify-content:center}
.card h3{font-size:14px;font-weight:800;text-transform:uppercase;line-height:1.2;margin-bottom:10px}
.card p{font-size:11px;line-height:1.6;color:var(--muted)}
.card.on{background:var(--green)}
.card.on h3,.card.on p{color:var(--white)}
.card.on .ic{background:rgba(255,255,255,.3)}

/* Experts */
.experts-img{left:0;top:2800px;width:600px;height:610px;background:linear-gradient(170deg,#8da6bc,#5a6f85 60%,#3b4a5a)}
.experts-panel{left:600px;top:2800px;width:600px;height:610px;background:linear-gradient(180deg,#2597de,#1678be);padding:70px 60px;color:var(--white)}
.experts-panel .h2{color:var(--white);font-size:40px;margin:8px 0 16px}
.experts-panel p{font-size:12px;line-height:1.7;opacity:.9;margin-bottom:16px}
.ex-item{display:flex;gap:12px;margin-bottom:14px}
.ex-item .tick{flex:none;width:18px;height:18px;border-radius:50%;background:var(--white);display:flex;align-items:center;justify-content:center}
.ex-item div{font-size:11px;line-height:1.6}
.ex-item b{font-weight:700}

/* Sustainable */
.sus-band{left:0;top:3440px;width:1200px;height:300px;background:var(--navy-2)}
.sus-head{left:0;top:3500px;width:1200px;text-align:center}
.sus-head .h2{color:var(--white);font-size:34px;margin-top:6px}
.sus-cards{left:140px;top:3620px;width:920px;display:flex;gap:20px}
.sc{flex:1}
.sc .pic{height:130px;border-radius:6px}
.sc h3{font-size:14px;font-weight:800;text-transform:uppercase;line-height:1.2;margin:18px 0 10px}
.sc p{font-size:11px;line-height:1.6;color:var(--muted)}

/* What is */
.what-text{left:180px;top:4040px;width:420px}
.what-text .h2{font-size:38px;margin:6px 0 14px}
.what-text .body{font-size:12px;line-height:1.65}
.what-list{margin-top:18px}
.what-list div{display:flex;align-items:center;gap:12px;font-size:13px;font-weight:800;text-transform:uppercase;margin-bottom:12px}
.what-list .dot{width:22px;height:22px;border-radius:50%;background:var(--blue);flex:none}
.what-img1{left:620px;top:4040px;width:210px;height:370px;background:linear-gradient(180deg,#2a3f66,#c46a3c 70%,#3a3030)}
.what-img2{left:850px;top:4140px;width:190px;height:270px;background:linear-gradient(180deg,#e7d9b8,#b98b5a)}

/* CTA */
.cta{left:0;top:4490px;width:1200px;height:450px;background:linear-gradient(180deg,#c7d2d9 0%,#dde4e6 40%,#8f8a7e 75%,#6b6254 100%)}
.cta-text{left:600px;top:4610px;width:540px}
.cta-text .h2{font-size:38px;margin:8px 0 14px}
.cta-text p{font-size:11px;line-height:1.6;color:#3f4650;margin-bottom:18px;width:440px}
.cta-text .btn{background:var(--blue)}

/* Footer */
.footer{left:0;top:4940px;width:1200px;height:360px;background:var(--navy)}
.f-logo{left:100px;top:5040px;width:260px}
.f-logo .name{font-size:34px;font-weight:800;color:var(--white);display:flex;align-items:center;gap:10px}
.f-logo .name .mark{width:18px;height:18px;border-radius:50%;background:var(--green)}
.f-logo .tag{font-size:12px;font-weight:600;color:var(--green);margin-top:4px}
.f-col{top:5000px;color:var(--white)}
.f-col h4{font-size:13px;font-weight:800;text-transform:uppercase;margin-bottom:6px}
.f-col .bar{width:30px;height:3px;background:var(--green);margin-bottom:16px}
.f-col li{list-style:none;font-size:12px;line-height:2;color:#c4ccd6}
.f-field{width:260px;height:38px;border-radius:4px;background:var(--white);font-size:11px;color:#999;padding:12px 14px;margin-bottom:12px}
.f-col .btn{background:var(--blue);padding:12px 22px;font-size:11px}
.copy{left:0;top:5300px;width:1200px;height:52px;background:#141e29;color:#b9c2cc;font-size:11px;display:flex;align-items:center;justify-content:space-between;padding:0 60px}
</style>
</head>
<body>

<section class="hero" role="img" aria-label="Industrial refinery plant lit at dusk against a blue sky">
  <div class="hero-shade"></div>
</section>
<header class="nav">
  <div class="logo"><span class="mark"></span>Vondrake</div>
  <nav class="menu">
    <span>Home</span><span>About Us</span><span>How It Works</span><span>Products</span><span>Impact</span><span>Team</span>
    <span class="btn">Contact Us</span>
  </nav>
</header>
<div class="hero-text">
  <div class="eyebrow">Welcome to Vondrake waste to fuel power</div>
  <h1>Transforming Plastic<br>Into Clean Diesel</h1>
  <p>At Vondrake we are pioneering a sustainable solution to plastic pollution by converting discarded plastic into high quality commercial diesel.</p>
  <span class="btn"><span class="dot"></span>Discover Our Process</span>
</div>

<div class="ph who-img1" role="img" aria-label="Scientist in a lab coat examining a sample"></div>
<div class="ph who-img2" role="img" aria-label="Clean energy facility under a blue sky"></div>
<div class="ph who-text">
  <div class="eyebrow">About Vondrake</div>
  <h2 class="h2">Who We Are</h2>
  <p class="body">Vondrake is an innovative energy company dedicated to turning discarded plastic waste into high quality diesel fuel. Our mission is to reduce environmental pollution while providing a dependable fuel for commercial use. We combine cutting edge technology with a commitment to real, lasting change.</p>
  <p class="body">At Vondrake we are revolutionizing the way energy is produced by turning plastic waste into high quality diesel fuel. Our innovative approach not only provides a sustainable and reliable fuel source for commercial use but also reduces harmful environmental pollution, combining state of the art technology with a deep commitment to responsibility.</p>
</div>

<section class="ph process">
  <div class="process-head">
    <div class="eyebrow">How it works</div>
    <h2 class="h2">Our Process</h2>
  </div>
  <div class="steps">
    <div class="step"><div class="num">01</div><h3>Collect and sort plastic waste</h3><p>We gather plastic waste from local sources and sort it by type to prepare it for efficient conversion.</p></div>
    <div class="step"><div class="num">02</div><h3>Convert plastic into diesel</h3><p>Using advanced low emission technology, the sorted plastic is broken down into crude fuel oil.</p></div>
    <div class="step"><div class="num">03</div><h3>Refine diesel to commercial grade quality</h3><p>The crude oil is refined and tested to meet commercial diesel standards.</p></div>
    <div class="step"><div class="num">04</div><h3>Deliver eco-friendly diesel to customers</h3><p>Finished diesel is delivered to businesses seeking a cleaner, reliable fuel supply.</p></div>
  </div>
</section>

<div class="ph quality-text">
  <div class="eyebrow">Our product</div>
  <h2 class="h2">High Quality<br>Commercial Diesel</h2>
  <p class="body">Our diesel meets strict standards for commercial vehicles, machinery and energy production. Every batch is tested to ensure consistent quality and a dependable supply for our partners.</p>
  <p class="body">Vondrake provides high quality, eco friendly diesel designed to meet the needs of commercial operations. By converting plastic waste into usable fuel, we help businesses cut their environmental footprint without losing power or efficiency.</p>
  <span class="btn" style="margin-top:8px"><span class="dot"></span>Get a Quote Today</span>
</div>
<div class="ph quality-frame"></div>
<div class="ph quality-img" role="img" aria-label="Fuel storage tanks at a refinery seen from above"></div>
<div class="ph badge"><b>25+</b><span>Years Experience</span></div>

<div class="ph impact-head">
  <div class="eyebrow">Our environmental impact</div>
  <h2 class="h2">Positive Impact On The Planet</h2>
  <p class="body">By converting plastic waste into diesel, Vondrake helps reduce plastic pollution, conserves natural resources and supports a cleaner environment. Every ton of diesel we produce is a step towards a sustainable future.</p>
</div>
<div class="ph cards">
  <div class="card"><div class="ic"><svg width="20" height="20" viewBox="0 0 20 20"><path d="M4 10l4 4 8-8" stroke="#8cc63f" stroke-width="2.5" fill="none"/></svg></div><h3>Reduces Plastic Pollution</h3><p>By converting discarded plastic into diesel, Vondrake prevents waste from ending up in landfills and oceans, directly combating environmental pollution.</p></div>
  <div class="card on"><div class="ic"><svg width="20" height="20" viewBox="0 0 20 20"><path d="M4 10l4 4 8-8" stroke="#fff" stroke-width="2.5" fill="none"/></svg></div><h3>Conserves Natural Resources</h3><p>Using recycled plastic as the feedstock for our diesel reduces reliance on crude oil and helps protect natural resources for future generations.</p></div>
  <div class="card"><div class="ic"><svg width="20" height="20" viewBox="0 0 20 20"><path d="M4 10l4 4 8-8" stroke="#8cc63f" stroke-width="2.5" fill="none"/></svg></div><h3>Supports a Cleaner Environment</h3><p>Our eco friendly process helps lower harmful emissions and contributes to a greener, healthier environment for communities and ecosystems.</p></div>
  <div class="card"><div class="ic"><svg width="20" height="20" viewBox="0 0 20 20"><path d="M4 10l4 4 8-8" stroke="#8cc63f" stroke-width="2.5" fill="none"/></svg></div><h3>Promotes Sustainable Energy</h3><p>Every ton of diesel we produce from plastic waste represents a step toward a renewable and sustainable energy future for businesses and the planet.</p></div>
</div>

<div class="ph experts-img" role="img" aria-label="Team of engineers in hard hats standing together at a plant"></div>
<section class="ph experts-panel">
  <div class="eyebrow">Meet the team</div>
  <h2 class="h2">Experts Driving<br>Innovation</h2>
  <p>Our team consists of environmental scientists, engineers and industry experts committed to sustainable energy solutions. With decades of combined experience, we are leading the way in waste to fuel conversion technology.</p>
  <div class="ex-item"><span class="tick"><svg width="10" height="10" viewBox="0 0 10 10"><path d="M2 5l2 2 4-4" stroke="#1e90d8" stroke-width="1.8" fill="none"/></svg></span><div><b>Environmental Scientists:</b> Our team includes environmental scientists dedicated to reducing waste and protecting the planet.</div></div>
  <div class="ex-item"><span class="tick"><svg width="10" height="10" viewBox="0 0 10 10"><path d="M2 5l2 2 4-4" stroke="#1e90d8" stroke-width="1.8" fill="none"/></svg></span><div><b>Innovative Engineers:</b> With years of combined experience, our technical experts design cutting edge conversion systems that turn plastic into diesel efficiently.</div></div>
  <div class="ex-item"><span class="tick"><svg width="10" height="10" viewBox="0 0 10 10"><path d="M2 5l2 2 4-4" stroke="#1e90d8" stroke-width="1.8" fill="none"/></svg></span><div><b>Commitment to Sustainability:</b> Every team member is dedicated to creating eco friendly solutions that reduce pollution and conserve resources.</div></div>
  <div class="ex-item"><span class="tick"><svg width="10" height="10" viewBox="0 0 10 10"><path d="M2 5l2 2 4-4" stroke="#1e90d8" stroke-width="1.8" fill="none"/></svg></span><div><b>Innovation &amp; Leadership:</b> We continually develop innovative processes and technologies to lead the sustainable fuel industry into a cleaner future.</div></div>
</section>

<div class="ph sus-band"></div>
<div class="ph sus-head">
  <div class="eyebrow">Our commitment</div>
  <h2 class="h2">Sustainable &amp; Responsible<br>Practices</h2>
</div>
<div class="ph sus-cards">
  <div class="sc"><div class="pic" role="img" aria-label="Workers sorting recyclable materials" style="background:linear-gradient(160deg,#9fb87a,#5f7a4a)"></div><h3>Environmental Responsibility</h3><p>We focus on reducing emissions and waste, making sure our operations follow strict environmental guidelines.</p></div>
  <div class="sc"><div class="pic" role="img" aria-label="Staff handling sustainable materials" style="background:linear-gradient(160deg,#c9b59a,#7d6a58)"></div><h3>Sustainable Materials</h3><p>We use green practices and recycled materials wherever possible to lower our environmental footprint.</p></div>
  <div class="sc"><div class="pic" role="img" aria-label="Community volunteers working outdoors" style="background:linear-gradient(160deg,#c48d86,#6f4f55)"></div><h3>Social Responsibility</h3><p>We are committed to employee well being, safe working environments and support for the communities we operate in.</p></div>
  <div class="sc"><div class="pic" role="img" aria-label="Fuel tanker trucks parked in a row" style="background:linear-gradient(160deg,#c25a52,#3e4a5e)"></div><h3>Governance &amp; Transparency</h3><p>We believe clear and open reporting builds accountability, trust and clear records across all business operations.</p></div>
</div>

<div class="ph what-text">
  <div class="eyebrow">About us</div>
  <h2 class="h2">What Is Orvane</h2>
  <p class="body">Orvane at Vondrake is our innovative solution for sustainable energy production. It is a cutting edge technology that efficiently converts plastic waste into high quality diesel fuel while minimizing environmental impact. Designed for commercial use, Orvane ensures consistent performance, reliability and eco friendly operation.</p>
  <div class="what-list">
    <div><span class="dot"></span>Efficient Conversion</div>
    <div><span class="dot"></span>Eco-Friendly Technology</div>
    <div><span class="dot"></span>Reliable Supply</div>
    <div><span class="dot"></span>Innovative &amp; Sustainable</div>
  </div>
</div>
<div class="ph what-img1" role="img" aria-label="Refinery towers at sunset"></div>
<div class="ph what-img2" role="img" aria-label="Engineer inspecting fuel samples"></div>

<section class="ph cta" role="img" aria-label="Bulldozer working on a plastic waste landfill"></section>
<div class="ph cta-text">
  <div class="eyebrow">Call to action for switching</div>
  <h2 class="h2">Ready To Switch To<br>Sustainable Diesel?</h2>
  <p>Contact Vondrake today to learn how your business can benefit from our eco friendly diesel.</p>
  <span class="btn"><span class="dot"></span>Contact Us</span>
</div>

<footer class="ph footer"></footer>
<div class="ph f-logo">
  <div class="name"><span class="mark"></span>Vondrake</div>
  <div class="tag">Waste to Fuel Power</div>
</div>
<div class="ph f-col" style="left:420px">
  <h4>Quick Links</h4><div class="bar"></div>
  <ul><li>Home</li><li>About Us</li><li>How It Works</li><li>Products</li><li>Impact</li><li>Team</li></ul>
</div>
<div class="ph f-col" style="left:580px">
  <h4>Contact Us</h4><div class="bar"></div>
  <ul><li>Address:</li><li>12 Harbor Works Lane, Eastfield</li><li>Phone:</li><li>+00 555 0148 220</li><li>Email:</li><li>hello@vondrake-fuel.com</li></ul>
</div>
<div class="ph f-col" style="left:840px">
  <h4>Subscribe Our Newsletter</h4><div class="bar"></div>
  <div class="f-field">Enter your email</div>
  <span class="btn"><span class="dot"></span>Subscribe</span>
</div>
<div class="ph copy"><span>Copyright © 2024 Vondrake All Rights Reserved</span><span>Privacy Policy | Terms of Condition</span></div>

</body>
</html>
```